依頼詳細
サイト構成・基本的な要件については
https://zenpiru.com/boards/kqTdnVxaPLmH52ze
を併せてご覧いただければ幸いです。

また、店舗写真・ロゴについては
http://nubalocker.jp/fetch/7b2e9d4a1c08f36e5d7a2b9c4e1f0a6d8c3b5e72
よりダウンロードいただければと存じます。

上記だけで制作が難しい場合は
http://mowlu.jp/
http://jp.gravenu.com/
http://www.lumivault.com/ja/cat-27-Beauty-Fashion.html
などから、10000円程度までならこちらにて購入可能です。
カンプデータにて作成頂き、
納品時に当方にて購入したデータに差し替えていただければと存じます。

ページ構成もシンプルですので
TOPページからすべての導線を配置するかたちでデザインいただければと存じます。
当方、jqueryなどのコーディングも対応可能ですので、
そういったデザイン提案を頂いても大丈夫です。

色合いは、店舗に合わせた、シンプルで明るい色合いを希望いたします。
木目、ブラウンを採用しているので、
そちらを展開した形のカラーパターンが合うかなと考えていますが、
特に絶対的な指定はありません。
サイトURL
http://beauty.kamobira.jp/slnH000583106/
ページ数
1ページ
希望イメージ
シンプル 複雑
単色 カラフル
暗い 明るい
日常 高級
遊び心 厳粛
未来的 伝統的
女性的 男性的
希望する色
茶系、店舗のイメージを展開するような色合いですと幸いです。
納品ファイル
• 高解像度JPG (.jpg)
• フォトショップ形式 (.psd)
補足説明
サイト構成・基本的な要件については
を併せてご覧いただければ幸いです。

また、写真・素材については
よりダウンロードいただければと存じます。

上記だけで制作が難しい場合は
http://mowlu.jp/
http://jp.gravenu.com/
などから、10000円程度までならこちらにて購入可能です。カンプデータにて作成頂き、納品時に当方にて購入したデータに差し替えていただければと存じます。

基本的には、大きなイメージ写真を前面に出して訴求しつつ
明るいイメージでまとめられればと思います。

【参考イメージ】
http://sumeragawa.jp/ (色合い、明るい印象)
http://www.bunaro.jp/home/studydesk/product/vomelq/(色合い、明るい印象)

余りかしこまった雰囲気にしてしまうよりは、柔らかく明るい印象にすることで、男女とも入りやすいサロンということをアピールできればと考えています。
制作につきましてご不明な点がございましたら、
お気軽にお申し付けいただければと存じます。
ご提案お待ちしております
ご質問にて、ワイヤーフレーム提示のご要望がありましたので追記いたします。

https://zenpiru.com/boards/hTrBnk3Yw9pLsd7c

上記が、当方で想定しているワイヤーですが、
あまり上記にこだわらず、ご提案頂ければ幸甚です。
ご不明な点がございましたらお気軽にお申し付けください。
http://nubalocker.jp/fetch/e5a08c2d7f91b3460ad2c8e17f59b04a26d3e8c1

念のため、素材を再アップいたします。

クライアントとの協議の結果、こちらの案を採用させていただきました。
スタイリッシュなデザインとサイト全体の見やすさ、信頼感、
文字などの読みやすさが大変気に入り、
そちらが採用の決め手となりました。

この度は多数ご提案いただきありがとうございました。
当選に至らなかったランサー様におかれましては大変心苦しいのですが、
次の機会にぜひご提案いただければ幸甚です。
引き続き何卒よろしくお願いいたします。

```html
<!DOCTYPE html>
<html lang="ja">
<head>
<meta charset="utf-8">
<title>CUT STUDIO LUMEN</title>
<link href="https://fonts.googleapis.com/css2?family=Noto+Sans+JP:wght@400;500;700&family=Noto+Serif+JP:wght@500;700&display=swap" rel="stylesheet">
<style>
:root{
  --brown:#6b4a2f;
  --brown-dark:#4e3522;
  --wood:#b98b5e;
  --cream:#f7f2ea;
  --green:#8cbf3f;
  --green-pale:#e4edd3;
  --orange:#e8821e;
  --pink:#ee6f8c;
  --text:#4a4038;
  --muted:#8a7e72;
  --line:#d9cfc3;
  --white:#ffffff;
}
*{margin:0;padding:0;box-sizing:border-box}
html,body{width:724px;height:1200px;overflow:hidden}
body{font-family:"Noto Sans JP",sans-serif;color:var(--text);background:var(--white);font-size:11px;position:relative}
.hero{position:absolute;left:0;top:0;width:724px;height:272px;background:linear-gradient(100deg,#7a5634 0%,#c9a57c 35%,#efe2cf 55%,#b48a5d 80%,#6e4a2c 100%)}
.brand{position:absolute;left:24px;top:30px;display:flex;align-items:center;gap:8px;font-family:"Noto Sans JP",sans-serif;font-weight:700;font-size:13px;color:var(--white);letter-spacing:.06em;white-space:nowrap}
.brand-dot{width:10px;height:10px;border-radius:50%;background:var(--white)}
.contact-box{position:absolute;right:24px;top:12px;width:184px;height:60px;background:rgba(78,53,34,.88);color:var(--white);padding:6px 10px;font-size:9px;line-height:1.45}
.contact-box .tel{font-size:15px;font-weight:700;letter-spacing:.04em;line-height:1.35;display:block}
.hero-copy{position:absolute;left:0;right:0;top:118px;text-align:center;color:var(--white);font-family:"Noto Serif JP",serif;font-size:15px;line-height:1.9;text-shadow:0 1px 3px rgba(0,0,0,.45)}
.global-nav{position:absolute;top:284px;left:0;width:724px;height:28px;border-top:1px solid var(--line);border-bottom:1px solid var(--line);display:flex;justify-content:center;align-items:center}
.global-nav a{color:var(--text);text-decoration:none;font-size:10.5px;padding:0 13px;border-left:1px solid var(--line)}
.global-nav a:last-child{border-right:1px solid var(--line)}
.welcome{position:absolute;top:340px;left:44px;width:640px;height:215px}
.welcome h1{font-family:"Noto Serif JP",serif;font-size:17px;color:var(--brown);font-weight:700}
.welcome .lead{color:var(--orange);font-size:11.5px;font-weight:700;margin:8px 0 10px}
.welcome p{font-size:9.5px;line-height:1.75;width:300px;margin-bottom:6px}
.welcome-photo{position:absolute;right:0;top:18px;width:314px;height:192px;background:linear-gradient(135deg,#efe6d8,#c7a57e 60%,#8a6440)}
.features{position:absolute;top:578px;left:0;width:724px;height:218px;background:var(--green-pale);display:flex;justify-content:center;gap:10px;align-items:center}
.feature{width:134px;height:134px;border-radius:50%;position:relative;display:flex;align-items:center;justify-content:center;color:var(--white);font-weight:700;font-size:12px;text-shadow:0 1px 2px rgba(0,0,0,.5)}
.f1{background:radial-gradient(circle,#d7b592,#8f6845)}
.f2{background:radial-gradient(circle,#f1f1ee,#c5c7c3)}
.f3{background:radial-gradient(circle,#e9cdb0,#a27a55)}
.f4{background:radial-gradient(circle,#c9ad8c,#6d4d32)}
.info{position:absolute;top:832px;left:110px;width:540px;height:180px}
.info-links{position:absolute;left:0;top:38px;width:150px}
.info-link{display:block;height:50px;margin-bottom:10px;position:relative;background:linear-gradient(90deg,#5d4a3a,#a88a6a)}
.info-link span{position:absolute;right:0;top:0;width:78px;height:50px;background:var(--green);color:var(--white);font-size:10px;display:flex;align-items:center;justify-content:center}
.news{position:absolute;left:192px;top:24px;width:348px}
.news h2{font-size:11.5px;color:var(--brown);font-weight:700;padding-bottom:6px;border-bottom:1px solid var(--line);margin-bottom:6px}
.news li{list-style:none;font-size:9px;line-height:2.1;border-bottom:1px dotted var(--line)}
.news time{color:var(--orange);margin-right:10px}
.more{position:absolute;right:0;top:152px;background:var(--brown);color:var(--white);font-size:8.5px;padding:3px 10px}
.to-top{position:absolute;right:22px;top:935px;width:28px;height:28px;border-radius:50%;background:var(--green)}
.footer-nav{position:absolute;top:1036px;left:0;width:724px;text-align:center;font-size:8.5px;color:var(--muted)}
.footer-nav .sub{margin-top:6px}
.site-footer{position:absolute;top:1088px;left:0;width:724px;height:112px;background:var(--brown);color:var(--white)}
.footer-name{position:absolute;left:24px;top:14px;font-size:10px;font-weight:700}
.footer-addr{position:absolute;left:24px;top:32px;font-size:8.5px;line-height:1.7}
.footer-tel{position:absolute;left:300px;top:14px;font-size:8.5px;line-height:1.8}
.reserve{position:absolute;right:24px;top:12px;width:170px;height:32px;background:var(--pink);color:var(--white);font-size:12px;font-weight:700;display:flex;align-items:center;justify-content:center}
.copy{position:absolute;bottom:10px;left:0;width:100%;text-align:center;font-size:7.5px;color:#e6d8c8}
</style>
</head>
<body>
<header class="hero" role="img" aria-label="木目調の明るいサロン店内の写真">
  <div class="brand"><span class="brand-dot"></span><span>CUT STUDIO LUMEN</span></div>
  <div class="contact-box">ご予約・お問い合わせ<span class="tel">03-4821-7730</span>営業時間 10:00〜20:00</div>
  <p class="hero-copy">メンズもレディースも気軽に通えるあたたかいサロン<br>木のぬくもりに包まれた空間で、心地よいひとときを。</p>
</header>

<nav class="global-nav">
  <a href="#">サロン案内</a><a href="#">メニュー・料金</a><a href="#">シャンプーについて</a><a href="#">スタッフ紹介</a><a href="#">よくある質問</a><a href="#">ギャラリー</a><a href="#">ご予約について</a>
</nav>

<section class="welcome">
  <h1>CUT STUDIO LUMENへようこそ</h1>
  <p class="lead">メンズもレディースもお気軽にお越しください！</p>
  <p>このたびはCUT STUDIO LUMENのホームページをご覧いただきありがとうございます。当店は木目とブラウンを基調にした、落ち着きのある明るいサロンです。</p>
  <p>お一人おひとりの髪質やライフスタイルに合わせて、再現しやすいスタイルをご提案いたします。初めての方も安心してご相談ください。</p>
  <p>皆さまのご来店をスタッフ一同、心よりお待ちしております。</p>
  <div class="welcome-photo" role="img" aria-label="鏡とスタイリングチェアのある店内の写真"></div>
</section>

<section class="features">
  <a class="feature f1" role="img" aria-label="サロン店内の写真">サロン案内</a>
  <a class="feature f2" role="img" aria-label="シャンプーボトルの写真">シャンプー</a>
  <a class="feature f3" role="img" aria-label="スタッフの後ろ姿の写真">スタッフ紹介</a>
  <a class="feature f4" role="img" aria-label="ヘアスタイルの写真">ギャラリー</a>
</section>

<section class="info">
  <div class="info-links">
    <a class="info-link" role="img" aria-label="受付カウンターの写真"><span>ご予約について</span></a>
    <a class="info-link" role="img" aria-label="店舗外観の写真"><span>店舗情報</span></a>
  </div>
  <div class="news">
    <h2>新着情報</h2>
    <ul>
      <li><time>2024.05.20</time>新着情報タイトルがここに入ります。</li>
      <li><time>2024.05.12</time>新着情報タイトルがここに入ります。</li>
      <li><time>2024.04.28</time>新着情報タイトルがここに入ります。</li>
      <li><time>2024.04.15</time>新着情報タイトルがここに入ります。</li>
    </ul>
  </div>
  <a class="more">一覧を見る</a>
</section>

<a class="to-top" aria-label="ページ上部へ">
  <svg width="28" height="28" viewBox="0 0 28 28"><path d="M9 16l5-5 5 5" fill="none" stroke="#fff" stroke-width="2"/></svg>
</a>

<div class="footer-nav">
  <p>サロン案内 | メニュー・料金 | シャンプーについて | スタッフ紹介 | よくある質問 | ギャラリー | ご予約について</p>
  <p class="sub">プライバシーポリシー | サイトマップ | お問い合わせ</p>
</div>

<footer class="site-footer">
  <p class="footer-name">CUT STUDIO LUMEN</p>
  <p class="footer-addr">〒102-0094<br>東京都千代田区紀尾町3-12 ルーメンビル1F</p>
  <p class="footer-tel">TEL：03-4821-7730<br>営業時間：10:00〜20:00（土日祝 9:00〜19:00）<br>定休日：毎週火曜日</p>
  <a class="reserve">ご予約はこちら</a>
  <p class="copy">Copyright (C) CUT STUDIO LUMEN All Rights Reserved.</p>
</footer>
</body>
</html>
```